Brix2Key Header

I want a professional Letterhead for my law firm. I'm attaching the letterhead I currently use in Word and PDF form. I'm also attaching my logo, and an example header that I like.

```html
<!DOCTYPE html>
<html lang="en">
<head>
<meta charset="utf-8">
<title>Brix2Key Letterhead</title>
<link href="https://fonts.googleapis.com/css2?family=Arimo:wght@400;700&family=Tinos:ital,wght@0,400;0,700;1,400&display=swap" rel="stylesheet">
<style>
  :root {
    --backdrop: #e9e9e9;
    --paper: #ffffff;
    --ink: #1a1a1a;
    --ink-soft: #3a3a3a;
    --brand-dark: #2f3033;
    --brand-blue: #0a6bbd;
    --brand-green: #3f9a3a;
    --rule-grey: #b9c6d6;
    --sig-blue: #5577c4;
  }
  * { box-sizing: border-box; margin: 0; padding: 0; }
  html, body { width: 1009px; height: 1200px; overflow: hidden; background: var(--backdrop); }
  .page {
    position: absolute; left: 94px; top: 20px;
    width: 820px; height: 1160px;
    background: var(--paper);
    box-shadow: 0 2px 10px rgba(0,0,0,.15);
    overflow: hidden;
    font-family: "Tinos", "Times New Roman", serif;
    color: var(--ink);
  }
  .abs { position: absolute; }

  /* Header */
  .brand { left: 16px; top: 38px; display: flex; align-items: center; gap: 10px; }
  .brand-mark { width: 18px; height: 18px; background: var(--brand-blue); }
  .brand-name {
    font-family: "Arimo", Arial, sans-serif; font-weight: 700;
    font-size: 50px; letter-spacing: -1px; color: var(--brand-dark); line-height: 1;
  }
  .contact { left: 561px; top: 11px; width: 232px; font-family: "Arimo", Arial, sans-serif; }
  .contact-name {
    font-family: "Tinos", "Times New Roman", serif;
    color: var(--brand-blue); font-size: 15.5px; text-align: center; letter-spacing: .2px;
  }
  .contact-firm { font-size: 12px; text-align: center; color: var(--ink-soft); margin-top: 2px; letter-spacing: .3px; }
  .contact-rule { height: 1px; background: var(--rule-grey); margin: 5px 0 6px; }
  .contact-grid {
    display: grid; grid-template-columns: 95px 1fr; row-gap: 5px;
    font-size: 10px; color: var(--ink-soft); padding-left: 5px;
  }
  .contact-item { display: flex; align-items: center; gap: 3px; white-space: nowrap; }
  .contact-item svg { width: 9px; height: 9px; flex: none; }
  .contact-address { font-size: 7.6px; text-align: center; color: var(--ink-soft); margin-top: 6px; letter-spacing: .1px; }
  .head-rule-blue { left: 0; top: 119px; width: 820px; height: 2px; background: var(--brand-blue); }
  .head-rule-green { left: 0; top: 124px; width: 820px; height: 2px; background: var(--brand-green); }

  /* Letter body */
  .letter-date { left: 0; top: 136px; width: 820px; text-align: center; font-weight: 700; font-size: 11.5px; font-variant: small-caps; }
  .recipient { left: 57px; top: 178px; font-size: 11.5px; line-height: 14.6px; }
  .recipient-via { font-weight: 700; font-style: italic; text-decoration: underline; font-variant: small-caps; }
  .subject { left: 109px; top: 280px; font-size: 11.5px; line-height: 14.6px; }
  .subject-label { position: absolute; left: 0; top: 0; font-weight: 700; font-variant: small-caps; }
  .subject-body { margin-left: 32px; }
  .subject-title { font-weight: 700; font-variant: small-caps; }
  .subject-row { display: grid; grid-template-columns: 105px 1fr; }
  .salutation { left: 57px; top: 352px; font-size: 11.5px; }

  .closing { left: 613px; top: 908px; font-size: 13.5px; line-height: 19px; }
  .signature { left: 597px; top: 930px; width: 140px; height: 60px;
    background: linear-gradient(90deg, rgba(85,119,196,.25), rgba(85,119,196,.08)); border-radius: 4px; }
  .signer { left: 613px; top: 984px; font-size: 13.5px; line-height: 19px; }
  .signer-title { font-style: italic; }

  /* Footer bands */
  .foot-band-blue { left: 553px; top: 1066px; width: 267px; height: 14px; background: var(--brand-blue); }
  .foot-band-green { left: 546px; top: 1087px; width: 274px; height: 14px; background: var(--brand-green); }
</style>
</head>
<body>
<main class="page">
  <header>
    <div class="abs brand">
      <span class="brand-mark"></span>
      <span class="brand-name">Brix2Key</span>
    </div>
    <div class="abs contact">
      <div class="contact-name">MARCUS T. DELGADO III</div>
      <div class="contact-firm">ATTORNEY AT LAW, PLLC</div>
      <div class="contact-rule"></div>
      <div class="contact-grid">
        <span class="contact-item"><svg viewBox="0 0 10 10"><circle cx="5" cy="5" r="5" fill="#3f9a3a"/><path d="M3.2 2.6l1 1-.5.7a3.5 3.5 0 0 0 2 2l.7-.5 1 1-.8.8C4.9 7.4 2.6 5.1 2.4 3.4z" fill="#fff"/></svg>(877) 555-0137</span>
        <span class="contact-item"><svg viewBox="0 0 10 10"><circle cx="5" cy="5" r="5" fill="#3f9a3a"/><rect x="2.5" y="3.2" width="5" height="3.6" fill="none" stroke="#fff" stroke-width=".8"/><path d="M2.5 3.2L5 5.2 7.5 3.2" fill="none" stroke="#fff" stroke-width=".8"/></svg>MARCUS@BRIX2KEY.NET</span>
        <span class="contact-item"><svg viewBox="0 0 10 10"><circle cx="5" cy="5" r="5" fill="#3f9a3a"/><rect x="2.6" y="3.6" width="4.8" height="2.8" fill="#fff"/><rect x="3.4" y="2.4" width="3.2" height="1.2" fill="#fff"/><rect x="3.4" y="6.6" width="3.2" height="1.2" fill="#fff"/></svg>(469) 555-0182</span>
        <span class="contact-item"><svg viewBox="0 0 10 10"><circle cx="5" cy="5" r="5" fill="#3f9a3a"/><circle cx="5" cy="5" r="2.8" fill="none" stroke="#fff" stroke-width=".7"/><path d="M2.2 5h5.6M5 2.2c-1.4 1.6-1.4 4 0 5.6M5 2.2c1.4 1.6 1.4 4 0 5.6" fill="none" stroke="#fff" stroke-width=".6"/></svg>WWW.BRIX2KEY.COM</span>
      </div>
      <div class="contact-rule" style="margin:6px 0 0"></div>
      <div class="contact-address">2450 ELMWOOD AVENUE SUITE 210 DALLAS, TEXAS 75204</div>
    </div>
    <div class="abs head-rule-blue"></div>
    <div class="abs head-rule-green"></div>
  </header>

  <section>
    <div class="abs letter-date">July 11, 2021</div>
    <div class="abs recipient">
      <div class="recipient-via">Via Facsimile: (800)-555-0142</div>
      <div>Harborline Insurance</div>
      <div>Attn: Peter Hale</div>
      <div>2210 Crestview Parkway 140</div>
      <div>Dallas, Texas 75234</div>
      <div>Tel: (972)-555-0190</div>
    </div>
    <div class="abs subject">
      <span class="subject-label">Re:</span>
      <div class="subject-body">
        <div class="subject-title">Notice of Representation</div>
        <div class="subject-row"><span>Claim Number:</span><span>1075710-TX</span></div>
        <div class="subject-row"><span>Date of Accident:</span><span>February 3, 2018</span></div>
        <div class="subject-row"><span>My client:</span><span>&nbsp;John Doe</span></div>
      </div>
    </div>
    <div class="abs salutation">Dear Mr. Peter Hale,</div>

    <div class="abs closing">Sincerely,</div>
    <div class="abs signature" role="img" aria-label="Handwritten signature of the attorney in blue ink"></div>
    <div class="abs signer">
      <div>Marcus T. Delgado</div>
      <div class="signer-title">Attorney at Law</div>
    </div>
  </section>

  <footer>
    <div class="abs foot-band-blue"></div>
    <div class="abs foot-band-green"></div>
  </footer>
</main>
</body>
</html>
```